New Business Card Design Project - RK Ledgerwise & Filing Partners, LLC

Below is a sample image of the card (TM Bookkeeping). I would like to have a designed business card that looks very similar (Front & Back). In addition, I would like to keep the same colors as well. I attached my Business Logo (RK Ledgerwise & Filing Partners, LLC) that will be on my website.

Target Market(s)

Executives, Business Owners, Board of Directors, Chief Financial Officers

Contact Information for Business Card

Font styles to use
Serif

Colors
0c5ba6
ffffff
5c5c5c

Requirements
Must have
• My Name: Malcolm Ferris, CPA
• Position: Owner
• Phone: (240) 555-0148
• Email: Mferris@rkledgerwise.example
• Website: www.Rkledgerwise.example
• Address: 4736 Ferncliff Ave #2093
• Dunmore Falls, MD 21990
Nice to have
• Same design & color scheme as TM Bookkeepnig Business card sample attached

```html
<!DOCTYPE html>
<html lang="en">
<head>
<meta charset="utf-8">
<title>RK Ledgerwise &amp; Filing Partners — Business Card</title>
<link href="https://fonts.googleapis.com/css2?family=PT+Serif:wght@400;700&display=swap" rel="stylesheet">
<style>
  :root {
    --page-bg: #e9e6e1;
    --card-dark: #1b1c1e;
    --card-light: #f2f2f2;
    --accent: #0c5ba6;
    --text-light: #ffffff;
    --text-grey: #5c5c5c;
    --divider: #8a8a8a;
  }
  * { margin: 0; padding: 0; box-sizing: border-box; }
  html, body {
    width: 1200px;
    height: 960px;
    overflow: hidden;
    background: var(--page-bg);
    font-family: "PT Serif", Georgia, serif;
  }
  .canvas { position: relative; width: 1200px; height: 960px; }

  .card {
    position: absolute;
    width: 600px;
    height: 342px;
    box-shadow: 0 3px 8px rgba(0,0,0,0.35);
  }
  .card--front { left: 314px; top: 113px; background: var(--card-dark); }
  .card--back  { left: 311px; top: 472px; height: 343px; background: var(--card-light); }

  /* Front */
  .identity {
    position: absolute;
    right: 322px;
    top: 153px;
    text-align: right;
  }
  .identity__name {
    color: var(--accent);
    font-size: 20px;
    font-weight: 700;
    line-height: 26px;
    white-space: nowrap;
  }
  .identity__title {
    color: var(--text-light);
    font-size: 14px;
    font-weight: 700;
    line-height: 18px;
  }
  .divider {
    position: absolute;
    left: 297px;
    top: 135px;
    width: 2px;
    height: 78px;
    background: linear-gradient(to bottom, transparent, var(--divider) 30%, #d0d0d0 50%, var(--divider) 70%, transparent);
  }
  .contacts {
    position: absolute;
    left: 321px;
    top: 147px;
    list-style: none;
  }
  .contacts__item {
    display: flex;
    align-items: center;
    height: 19px;
    color: var(--text-light);
    font-size: 14px;
    white-space: nowrap;
  }
  .contacts__icon { width: 14px; height: 14px; margin-right: 7px; fill: var(--accent); flex: none; }
  .address {
    position: absolute;
    left: 0;
    right: 0;
    top: 294px;
    display: flex;
    justify-content: center;
    align-items: center;
    color: var(--text-light);
    font-size: 14px;
    white-space: nowrap;
  }
  .address__icon { width: 12px; height: 16px; margin-right: 7px; fill: var(--accent); }

  /* Back */
  .brand-name {
    position: absolute;
    left: 0;
    right: 0;
    top: 155px;
    text-align: center;
    color: var(--accent);
    font-size: 19px;
    font-weight: 400;
    letter-spacing: 1.5px;
    text-transform: uppercase;
    white-space: nowrap;
  }
  .website {
    position: absolute;
    left: 0;
    right: 0;
    top: 274px;
    text-align: center;
    color: var(--text-grey);
    font-size: 14px;
    letter-spacing: 4.2px;
    white-space: nowrap;
  }
</style>
</head>
<body>
<main class="canvas">
  <section class="card card--front" aria-label="Card front">
    <div class="identity">
      <p class="identity__name">Malcolm Ferris, CPA</p>
      <p class="identity__title">Owner</p>
    </div>
    <div class="divider"></div>
    <ul class="contacts">
      <li class="contacts__item">
        <svg class="contacts__icon" viewBox="0 0 24 24" aria-hidden="true"><path d="M6.6 10.8a15.2 15.2 0 0 0 6.6 6.6l2.2-2.2c.3-.3.7-.4 1-.2 1.1.4 2.3.6 3.6.6.6 0 1 .4 1 1V20c0 .6-.4 1-1 1A17 17 0 0 1 3 4c0-.6.4-1 1-1h3.5c.6 0 1 .4 1 1 0 1.3.2 2.5.6 3.6.1.3 0 .7-.2 1z"/></svg>
        (240) 555-0148
      </li>
      <li class="contacts__item">
        <svg class="contacts__icon" viewBox="0 0 24 24" aria-hidden="true"><path d="M2 5h20v14H2z"/><path d="M3 6l9 6.3L21 6v-.5H3z" fill="#1b1c1e"/></svg>
        Mferris@rkledgerwise.example
      </li>
      <li class="contacts__item">
        <svg class="contacts__icon" viewBox="0 0 24 24" aria-hidden="true"><circle cx="12" cy="12" r="10"/><path d="M7 7c2 0 3 1 3 2s-2 1-2 3 2 2 2 4M15 5c-1 2 1 3 3 3M14 14c1 0 3 1 2 4" stroke="#1b1c1e" stroke-width="1.6" fill="none"/></svg>
        www.Rkledgerwise.example
      </li>
    </ul>
    <p class="address">
      <svg class="address__icon" viewBox="0 0 12 16" aria-hidden="true"><path d="M6 0a6 6 0 0 1 6 6c0 4-6 10-6 10S0 10 0 6a6 6 0 0 1 6-6zm0 3.5a2.5 2.5 0 1 0 0 5 2.5 2.5 0 0 0 0-5z" fill-rule="evenodd"/></svg>
      4736 Ferncliff Ave #2093 Dunmore Falls, MD 21990
    </p>
  </section>

  <section class="card card--back" aria-label="Card back">
    <p class="brand-name">RK Ledgerwise &amp; Filing Partners</p>
    <p class="website">www.Rkledgerwise.example</p>
  </section>
</main>
</body>
</html>
```